Cedarbrook Lane Allies Stationery

Use attached logo for stationery
Stationery, Letterhead and Envelope + Business cards

Tag line: Standing beside those who serve their neighbors well

```html
<!DOCTYPE html>
<html lang="en">
<head>
<meta charset="utf-8">
<title>Cedarbrook Lane Allies – Business Card</title>
<link href="https://fonts.googleapis.com/css2?family=Open+Sans:wght@400;600;700&family=Titillium+Web:wght@400&display=swap" rel="stylesheet">
<style>
  :root {
    --backdrop: #a4a4a4;
    --card-light: #eceeef;
    --navy: #0e4a8c;
    --navy-deep: #0a3f7d;
    --sky: #63c3ea;
    --text-grey: #555a5f;
    --sun: #f5c21b;
    --white: #ffffff;
  }
  * { margin: 0; padding: 0; box-sizing: border-box; }
  html, body { width: 1200px; height: 1200px; overflow: hidden; }
  body { background: var(--backdrop); position: relative; font-family: "Open Sans", sans-serif; }

  .card { position: absolute; left: 204px; width: 794px; height: 456px; border-radius: 24px; overflow: hidden; }

  /* front */
  .card-front { top: 90px; background: var(--card-light); }
  .brand-mark { position: absolute; right: 42px; top: 150px; display: flex; align-items: center; gap: 12px; }
  .brand-dot { width: 22px; height: 22px; border-radius: 50%; background: var(--sun); }
  .brand-name { font-family: "Open Sans", sans-serif; font-weight: 600; font-size: 30px; color: var(--navy); letter-spacing: 0.5px; }

  .person { position: absolute; left: 42px; top: 222px; }
  .person-name { font-weight: 700; font-size: 26px; color: var(--navy); letter-spacing: 0.3px; }
  .person-role { font-family: "Titillium Web", sans-serif; font-size: 17px; color: var(--text-grey); margin-top: 2px; }

  .divider { position: absolute; left: 42px; right: 42px; top: 300px; height: 2px; background: var(--sky); opacity: 0.8; }

  .contact-list { position: absolute; left: 42px; top: 319px; list-style: none; }
  .contact-list li { display: flex; align-items: center; gap: 10px; height: 28.5px; font-family: "Titillium Web", sans-serif; font-size: 17px; color: var(--text-grey); }
  .contact-list svg { width: 16px; height: 16px; fill: var(--sky); flex: none; }

  .address { position: absolute; right: 42px; top: 319px; text-align: right; font-family: "Titillium Web", sans-serif; font-size: 17px; color: var(--text-grey); line-height: 28.5px; }
  .address-org { color: var(--navy); }
  .address-org span { color: var(--sky); }

  .footer-band { position: absolute; left: 0; bottom: 0; width: 794px; height: 45px; }
  .website { position: absolute; right: 42px; bottom: 9px; font-family: "Titillium Web", sans-serif; font-size: 16px; color: var(--white); }

  /* back */
  .card-back { top: 656px; background: linear-gradient(180deg, var(--navy) 0%, var(--navy-deep) 100%); }
  .back-brand { position: absolute; left: 0; right: 0; top: 262px; text-align: center; font-weight: 600; font-size: 44px; color: var(--white); letter-spacing: 1px; }
  .tagline { position: absolute; left: 0; right: 0; top: 395px; text-align: center; font-family: "Titillium Web", sans-serif; font-size: 17px; color: var(--white); }
</style>
</head>
<body>

<section class="card card-front">
  <div class="brand-mark">
    <span class="brand-dot"></span>
    <span class="brand-name">Cedarbrook Lane Allies</span>
  </div>

  <div class="person">
    <h1 class="person-name">DANIEL R. HOLLIS</h1>
    <p class="person-role">Resident Manager</p>
  </div>

  <div class="divider"></div>

  <ul class="contact-list">
    <li>
      <svg viewBox="0 0 24 24" aria-hidden="true"><path d="M6.6 10.8a15.1 15.1 0 0 0 6.6 6.6l2.2-2.2a1 1 0 0 1 1-.25 11.4 11.4 0 0 0 3.6.57 1 1 0 0 1 1 1V20a1 1 0 0 1-1 1A17 17 0 0 1 3 4a1 1 0 0 1 1-1h3.5a1 1 0 0 1 1 1c0 1.25.2 2.45.57 3.57a1 1 0 0 1-.25 1z"/></svg>
      (555) 410-3872
    </li>
    <li>
      <svg viewBox="0 0 24 24" aria-hidden="true"><path d="M7 3h10v4H7zM4 8h16a2 2 0 0 1 2 2v6h-4v5H6v-5H2v-6a2 2 0 0 1 2-2zm4 8v3h8v-3z"/></svg>
      (555) 410-3872
    </li>
    <li>
      <svg viewBox="0 0 24 24" aria-hidden="true"><path d="M2 5h20v14H2zm2 2v.4l8 5.2 8-5.2V7zm0 2.8V17h16V9.8l-8 5.2z"/></svg>
      info@cedarbrooklaneallies.org
    </li>
  </ul>

  <div class="address">
    <p class="address-org">Cedarbrook Lane <span>Allies</span></p>
    <p>48 B Orchard Crest Lane</p>
    <p>Millbrook, SC 29100</p>
  </div>

  <svg class="footer-band" viewBox="0 0 794 45" preserveAspectRatio="none" aria-hidden="true">
    <path d="M0 3 H470 L470 10 H0 Z" fill="var(--sky)"/>
    <path d="M0 11 H455 C 490 11, 500 -2, 540 -2 H794 V45 H0 Z" fill="var(--navy)"/>
  </svg>
  <p class="website">www.cedarbrooklaneallies.org</p>
</section>

<section class="card card-back">
  <p class="back-brand">Cedarbrook Lane Allies</p>
  <p class="tagline">Standing beside those who serve their neighbors well</p>
</section>

</body>
</html>
```